Business Cards that are elegant and wow

I want to create and print business cards that represent my brand and stand out from the rest. We want to ensure they stay in our branding and the integrity is not lost. I am happy to look at different shapes like square etc.

It will be printed on very thick cards and will be stylish .

I want to create and print business cards that represent my brand and stand out from the rest. We want to ensure they stay in ur branding and the integrity is not lost. I am happy to look at different shapes like square etc.

Target Market(s)

real estate professionals

Industry/Entity Type

Real Estate

Contact Information for Business Card

Maren Holt
hello@brightfernrealty.com.au
brightfernrealty.com.au
0487 316 252 (SMS)

Colors

Designer to choose colors to be used in the design.

Requirements
Must have
• My logo
• email
• website
• Name
Nice to have
• I like the idea of printing with foil or spot gloss. You want it to stand out in a sea.
Should not have
• I would like you to stay in my colour themes. Don't change the colour of my logo

```html
<!DOCTYPE html>
<html lang="en">
<head>
<meta charset="utf-8">
<title>Bright Fern Realty — Business Card</title>
<link rel="stylesheet" href="https://fonts.googleapis.com/css2?family=Montserrat:wght@500;600;700&display=swap">
<style>
  :root {
    --backdrop: #b1b1b0;
    --brand-pink: #ee107a;
    --brand-blue: #00aeef;
    --paper: #ffffff;
    --sliver: #e3e3e3;
  }
  html, body {
    margin: 0;
    padding: 0;
    width: 1200px;
    height: 1200px;
    overflow: hidden;
    background: var(--backdrop);
  }
  .canvas {
    position: relative;
    width: 1200px;
    height: 1200px;
  }
  .card {
    position: absolute;
    left: 367px;
    width: 502px;
    height: 294px;
    display: block;
  }
  .card--front { top: 231px; }
  .card--back { top: 634px; }
  .card text {
    font-family: "Montserrat", sans-serif;
  }
  .wordmark-front { fill: var(--paper); font-weight: 600; font-size: 30px; }
  .holder-name { fill: var(--brand-blue); font-weight: 700; font-size: 46px; letter-spacing: -0.5px; }
  .contact-line { fill: var(--paper); font-weight: 500; font-size: 15px; }
  .contact-icon { fill: var(--paper); }
  .wordmark-back { fill: var(--brand-blue); font-weight: 600; font-size: 19px; }
</style>
</head>
<body>
<main class="canvas">

  <!-- Front of card -->
  <svg class="card card--front" viewBox="0 0 627 368" xmlns="http://www.w3.org/2000/svg">
    <defs>
      <clipPath id="front-edge"><rect width="627" height="368"/></clipPath>
    </defs>
    <rect class="front-field" width="627" height="368" fill="var(--brand-pink)"/>
    <circle class="front-disc" cx="446" cy="184" r="192" fill="var(--brand-blue)" clip-path="url(#front-edge)"/>
    <text class="wordmark-front" x="38" y="306">BRIGHT FERN</text>
    <text class="wordmark-front" x="38" y="340">REALTY</text>
  </svg>

  <!-- Back of card -->
  <svg class="card card--back" viewBox="0 0 627 368" xmlns="http://www.w3.org/2000/svg">
    <rect class="back-field" width="627" height="368" fill="var(--paper)"/>
    <polygon class="band-blue" points="0,240 447,115 305,368 0,368" fill="var(--brand-blue)"/>
    <polygon class="sliver-top" points="478,0 517,0 447,115" fill="var(--sliver)"/>
    <polygon class="sliver-bottom" points="447,115 333,368 305,368" fill="var(--sliver)"/>
    <polygon class="corner-pink" points="517,0 627,0 627,102 447,115" fill="var(--brand-pink)"/>

    <text class="holder-name" x="52" y="115">MAREN HOLT</text>

    <!-- phone -->
    <path class="contact-icon" d="M65,243 l3,-1 l2,4 l-2,1.5 q1,3 3.5,5 l1.5,-1.5 l3.5,2.5 l-1,2.5 q-4,1 -8,-5 q-4,-5 -2.5,-8 z"/>
    <text class="contact-line" x="100" y="254">0487 316 252 (SMS)</text>

    <!-- email -->
    <rect class="contact-icon" x="63" y="275" width="11" height="8" rx="1"/>
    <path d="M63.5,275.5 l5,4 l5,-4" fill="none" stroke="var(--brand-blue)" stroke-width="1"/>
    <text class="contact-line" x="100" y="283">hello@brightfernrealty.com.au</text>

    <!-- web -->
    <circle cx="68.5" cy="309" r="5.5" fill="none" stroke="var(--paper)" stroke-width="1.3"/>
    <ellipse cx="68.5" cy="309" rx="2.3" ry="5.5" fill="none" stroke="var(--paper)" stroke-width="1"/>
    <line x1="63" y1="309" x2="74" y2="309" stroke="var(--paper)" stroke-width="1"/>
    <text class="contact-line" x="100" y="314">brightfernrealty.com.au</text>

    <!-- brand block -->
    <circle class="brand-dot" cx="401" cy="290" r="23" fill="none" stroke="var(--brand-pink)" stroke-width="3"/>
    <text class="wordmark-back" x="434" y="286">BRIGHT FERN</text>
    <text class="wordmark-back" x="434" y="308">REALTY</text>
  </svg>

</main>
</body>
</html>
```